Brochure Design

We need a 6 page Brochure designed for our product, please see attached document for more information. The content should focus on account work.

Target Market(s)

Businesses that use a taxi service for their business

Requirements
Must have
• Must have key content on the services we provide for Account work

```html
<!DOCTYPE html>
<html lang="en">
<head>
<meta charset="utf-8">
<title>Rydo Brochure – Cover &amp; Back Cover</title>
<link rel="stylesheet" href="https://fonts.googleapis.com/css2?family=Montserrat:wght@300;400;500;700;800&display=swap">
<style>
  :root {
    --stage: #080d17;
    --yellow: #fdb81b;
    --beige: #e9dccb;
    --beige-deep: #cdbba5;
    --ink: #141414;
    --white: #ffffff;
    --night: #2a2d33;
    --amber: #b58a12;
  }
  * { margin: 0; padding: 0; box-sizing: border-box; }
  html, body { width: 1200px; height: 1200px; overflow: hidden; background: var(--stage); }
  body { position: relative; font-family: "Montserrat", Arial, sans-serif; }

  .board-title {
    position: absolute; top: 118px; left: 0; width: 1200px;
    text-align: center; color: var(--white);
    font-weight: 300; font-size: 30px; letter-spacing: 0.5px;
  }

  .spread { position: absolute; top: 246px; left: 90px; width: 1021px; height: 722px; display: flex; }

  /* Back cover */
  .back-cover { position: relative; width: 510px; height: 722px; overflow: hidden; background: var(--beige); }
  .back-photo {
    position: absolute; inset: 110px 0 0 0;
    background: linear-gradient(160deg, #efe4d6 0%, #e2d3c0 45%, #c9b59c 100%);
  }
  .phone-photo {
    position: absolute; left: 205px; top: 455px; width: 305px; height: 267px;
    background: radial-gradient(ellipse at 45% 40%, #f2c230 0%, #d99f6f 45%, rgba(201,170,140,0) 75%);
  }
  .top-band { position: absolute; top: 0; left: 0; width: 100%; height: 110px; background: var(--yellow); }
  .logo-disc {
    position: absolute; left: 195px; top: 53px; width: 122px; height: 122px;
    border-radius: 50%; background: var(--beige);
  }
  .brand-mark {
    position: absolute; left: 0; top: 95px; width: 100%;
    display: flex; align-items: center; justify-content: center; gap: 8px;
    color: var(--ink); font-weight: 800; font-size: 34px;
  }
  .brand-mark .dot { width: 16px; height: 16px; border-radius: 50%; background: var(--ink); }

  .contact { position: absolute; left: 0; width: 100%; text-align: center; color: var(--ink); font-size: 8.6px; line-height: 12px; }
  .divider { display: flex; align-items: center; justify-content: center; gap: 5px; height: 16px; }
  .divider::before, .divider::after { content: ""; width: 24px; height: 1px; background: var(--ink); }
  .divider svg { width: 13px; height: 13px; }
  .contact p { margin-top: 6px; }
  .contact-address { top: 210px; }
  .contact-phone { top: 304px; }
  .contact-mail { top: 360px; }

  /* Front cover */
  .front-cover { position: relative; width: 511px; height: 722px; overflow: hidden; }
  .street-photo {
    position: absolute; inset: 0;
    background:
      radial-gradient(ellipse at 52% 62%, rgba(255,200,120,0.55) 0%, rgba(255,200,120,0) 30%),
      linear-gradient(180deg, #3a3c40 0%, #2b2c2f 45%, #1e1f22 62%, #8a6a10 78%, #b58a12 100%);
  }
  .headline { position: absolute; left: 42px; top: 30px; color: var(--white); font-size: 42px; line-height: 50px; }
  .headline .light { font-weight: 300; display: block; }
  .headline .strong { font-weight: 800; display: block; }
  .front-brand {
    position: absolute; left: 42px; top: 880px; top: 636px;
    display: flex; align-items: center; gap: 6px;
    color: var(--white); font-weight: 800; font-size: 24px;
  }
  .front-brand .dot { width: 12px; height: 12px; border-radius: 50%; background: var(--white); }
  .web-pill {
    position: absolute; right: 0; top: 672px; width: 118px; height: 19px;
    background: var(--yellow); border-radius: 8px 0 0 8px;
    color: var(--ink); font-size: 8.6px; font-weight: 600; line-height: 19px; text-align: center;
  }
</style>
</head>
<body>
  <h1 class="board-title">Cover &amp; Back Cover</h1>

  <div class="spread">
    <section class="back-cover">
      <div class="back-photo" role="img" aria-label="Softly blurred stone pavement in warm beige light"></div>
      <div class="phone-photo" role="img" aria-label="Hand holding a smartphone with a small yellow taxi standing on its screen"></div>
      <div class="top-band"></div>
      <div class="logo-disc"></div>
      <div class="brand-mark"><span class="dot"></span>Rydo</div>

      <div class="contact contact-address">
        <div class="divider">
          <svg viewBox="0 0 12 12"><path d="M6 1a3.5 3.5 0 0 0-3.5 3.5C2.5 7.3 6 11 6 11s3.5-3.7 3.5-6.5A3.5 3.5 0 0 0 6 1z" fill="none" stroke="#141414" stroke-width="1"/><circle cx="6" cy="4.5" r="1.4" fill="#141414"/></svg>
        </div>
        <p>Velmora Tech Limited,<br>The Foundry Hub,<br>Northgate Innovation Park,<br>Larch Way, Eastbury.<br>EB4 7QL.</p>
      </div>

      <div class="contact contact-phone">
        <div class="divider">
          <svg viewBox="0 0 12 12"><path d="M3 1.5l1.6 2.3-1 1c.6 1.4 1.6 2.4 3 3l1-1 2.3 1.6-.8 1.6C5.4 10 2 6.6 1.5 2.3z" fill="#141414"/></svg>
        </div>
        <p>+1 (555) 014 2298</p>
      </div>

      <div class="contact contact-mail">
        <div class="divider">
          <svg viewBox="0 0 12 12"><rect x="1" y="2.5" width="10" height="7" fill="#141414"/><path d="M1 2.5l5 4 5-4" fill="none" stroke="#e9dccb" stroke-width="0.9"/></svg>
        </div>
        <p>hello@rydo.cab</p>
      </div>
    </section>

    <section class="front-cover">
      <div class="street-photo" role="img" aria-label="City street between tall buildings at sunset with a yellow taxi in the foreground"></div>
      <h2 class="headline">
        <span class="light">Exceptional</span>
        <span class="light">Travel</span>
        <span class="light">for a</span>
        <span class="strong">MODERN</span>
        <span class="strong">BUSINESS</span>
      </h2>
      <div class="front-brand"><span class="dot"></span>Rydo</div>
      <div class="web-pill">www.rydo.cab</div>
    </section>
  </div>
</body>
</html>
```